Financial Service Company Need Business Card Design

This is a new startup company, first of its kind to offer this service. We facilitate the movement of deposit funds electronically between home buyers and real estate brokerages.Our customers are REALTORS®, real estate brokerages, and home buyers, we identify ourselves as a financial/technology company.
Not looking for anything too flashy. Just a clean design that shows the logo, contact info, etc. Company colors can be seen on attached logo, and 'coming soon page'
www.plumvault.ca
Industry/Entity Type
Business
Contact Information for Business Card

```html
<!DOCTYPE html>
<html lang="en">
<head>
<meta charset="utf-8">
<title>PlumVault Business Card</title>
<link href="https://fonts.googleapis.com/css2?family=Open+Sans:wght@400;600;700&display=swap" rel="stylesheet">
<style>
  :root {
    --page-bg: #e4e4e2;
    --card-light: #a3a4a6;
    --card-mid: #8b8c8e;
    --card-dark: #737476;
    --slit-dark: #2c2d2f;
    --text-white: #f4f4f4;
    --accent-orange: #e8703a;
    --accent-blue: #4fb6e0;
    --icon-white: #f0f0f0;
  }
  * { box-sizing: border-box; margin: 0; padding: 0; }
  html, body {
    width: 1200px; height: 800px; overflow: hidden;
    background: var(--page-bg);
    font-family: "Open Sans", Arial, sans-serif;
  }
  .canvas { position: relative; width: 1200px; height: 800px; }

  .card {
    position: absolute; top: 250px;
    width: 525px; height: 300px;
    overflow: hidden;
    background: linear-gradient(160deg, var(--card-light) 0%, var(--card-mid) 45%, var(--card-dark) 100%);
    box-shadow: 0 6px 18px rgba(0,0,0,0.22);
  }
  .card-front { left: 50px; }
  .card-back { left: 625px; }

  /* recessed slit behind the brand */
  .brand-slit {
    position: absolute; left: 30px; top: 112px;
    width: 470px; height: 74px;
    transform: rotate(-4deg);
    background: radial-gradient(ellipse at center, rgba(40,41,43,0.55) 0%, rgba(40,41,43,0.25) 45%, rgba(40,41,43,0) 72%);
  }
  .brand-slit::before {
    content: ""; position: absolute; left: 10%; right: 4%; top: 6px; height: 3px;
    background: linear-gradient(90deg, transparent, var(--slit-dark) 30%, var(--slit-dark) 75%, transparent);
    filter: blur(1px);
  }
  .brand-slit::after {
    content: ""; position: absolute; left: 14%; right: 12%; bottom: 4px; height: 2px;
    background: linear-gradient(90deg, transparent, rgba(230,230,230,0.7) 40%, transparent);
  }
  .brand {
    position: absolute; left: 92px; top: 122px;
    display: flex; align-items: center; gap: 12px;
    transform: rotate(-4deg);
  }
  .brand-mark { width: 30px; height: 30px; background: var(--accent-orange); }
  .brand-name {
    font-size: 44px; font-weight: 700; color: var(--text-white); letter-spacing: 0.5px; line-height: 1;
  }
  .brand-url {
    position: absolute; left: 150px; top: 188px;
    transform: rotate(-4deg);
    font-size: 19px; font-weight: 700; color: var(--accent-orange); letter-spacing: 1px;
  }

  /* back side */
  .identity { position: absolute; left: 34px; top: 86px; }
  .person-name { font-size: 22px; font-weight: 600; color: var(--text-white); letter-spacing: 1px; }
  .person-role { font-size: 20px; font-weight: 400; color: var(--accent-blue); letter-spacing: 1.5px; margin-top: -2px; }

  .divider-slit {
    position: absolute; left: 262px; top: -20px;
    width: 46px; height: 340px;
    transform: rotate(14deg);
    background: radial-gradient(ellipse at center, rgba(40,41,43,0.5) 0%, rgba(40,41,43,0.18) 45%, rgba(40,41,43,0) 72%);
  }
  .divider-slit::before {
    content: ""; position: absolute; top: 10%; bottom: 10%; left: 22px; width: 2px;
    background: linear-gradient(180deg, transparent, var(--slit-dark) 30%, var(--slit-dark) 70%, transparent);
  }

  .contact-icons { position: absolute; left: 228px; top: 92px; display: flex; flex-direction: column; gap: 36px; }
  .contact-icons svg { width: 24px; height: 24px; display: block; }
  .contact-list { position: absolute; left: 330px; top: 100px; list-style: none; }
  .contact-list li { font-size: 15px; line-height: 1; color: var(--text-white); margin-bottom: 40px; }
  .contact-list .contact-phone { font-size: 17px; font-weight: 600; }
  .contact-list .contact-web { color: var(--accent-blue); }
</style>
</head>
<body>
<main class="canvas">
  <section class="card card-front" aria-label="Card front">
    <div class="brand-slit"></div>
    <div class="brand">
      <span class="brand-mark"></span>
      <span class="brand-name">PlumVault</span>
    </div>
    <p class="brand-url">www.plumvault.ca</p>
  </section>

  <section class="card card-back" aria-label="Card back">
    <div class="identity">
      <p class="person-name">NAME SURNAME</p>
      <p class="person-role">OCCUPATION</p>
    </div>
    <div class="divider-slit"></div>
    <div class="contact-icons">
      <svg viewBox="0 0 24 24" aria-label="Phone" role="img">
        <path d="M6.5 3h3l1.5 4-2 1.5a11 11 0 0 0 6.5 6.5l1.5-2 4 1.5v3a2 2 0 0 1-2 2A17 17 0 0 1 4.5 5a2 2 0 0 1 2-2z" fill="none" stroke="var(--icon-white)" stroke-width="1.6" stroke-linejoin="round"/>
      </svg>
      <svg viewBox="0 0 24 24" aria-label="Website" role="img">
        <g fill="none" stroke="var(--accent-blue)" stroke-width="1.6">
          <circle cx="12" cy="12" r="9.5"/>
          <ellipse cx="12" cy="12" rx="4.2" ry="9.5"/>
          <line x1="2.5" y1="12" x2="21.5" y2="12"/>
          <path d="M4.5 7h15M4.5 17h15"/>
        </g>
      </svg>
    </div>
    <ul class="contact-list">
      <li class="contact-phone">123 456 789</li>
      <li class="contact-web">www.plumvault.ca</li>
      <li class="contact-email">contact@email.com</li>
    </ul>
  </section>
</main>
</body>
</html>
```